Criminal Defense Law firm Billboard Design

We need a billboard to occupy a board space we have ASAP. Would like it to convey our lawfirm's brand. qrlegalshield.com is our website where you can see the colors we use, blues, etc. We have high rez pictures of both attorneys for you to use, just request them. We would like CRIMINAL AND PROBATION DEFENSE to be prominent on this display. We would also like our primary office # along with a second number for Spanish speakers to be displayed.

Target Market(s)

traffic in Cumming, GA

Industry/Entity Type

attorney-legal

Colors
0054AA
0677BA
7BADD7
CADEEF
E8F1F8

Requirements
Must have
• Awesome design that will attract customers

```html
<!DOCTYPE html>
<html lang="en">
<head>
<meta charset="utf-8">
<title>Quarry Reed – Criminal and Probation Defense Billboard</title>
<link rel="stylesheet" href="https://fonts.googleapis.com/css2?family=Tinos:wght@400;700&display=swap">
<style>
  :root {
    --brand-blue: #0054aa;
    --brand-blue-deep: #0a4fa8;
    --brand-mid: #0677ba;
    --brand-light: #7badd7;
    --brand-pale: #cadeef;
    --brand-mist: #e8f1f8;
    --white: #ffffff;
    --frame: #2b2b2b;
    --page: #eef1f4;
  }
  * { margin: 0; padding: 0; box-sizing: border-box; }
  html, body {
    width: 1200px;
    height: 598px;
    overflow: hidden;
    background: var(--page);
  }
  .canvas {
    position: relative;
    width: 1200px;
    height: 598px;
  }
  .billboard {
    position: absolute;
    left: 20px;
    top: 125px;
    width: 1259px;
    height: 378px;
    transform: scale(0.9214);
    transform-origin: top left;
    background: var(--brand-blue);
    overflow: hidden;
    font-family: "Tinos", "Times New Roman", serif;
    color: var(--white);
  }
  .headline-band {
    position: absolute;
    left: 0;
    top: 156px;
    width: 100%;
    height: 126px;
    background: linear-gradient(90deg,
      rgba(255,255,255,0) 0px,
      rgba(255,255,255,0) 380px,
      var(--brand-pale) 430px,
      var(--white) 520px,
      var(--white) 100%);
  }
  .band-fade {
    position: absolute;
    left: 0;
    top: 156px;
    width: 430px;
    height: 126px;
    background: linear-gradient(90deg, var(--brand-blue) 0%, #2a6fc0 100%);
    opacity: 0.6;
  }
  .accent-rule {
    position: absolute;
    left: 0;
    top: 56px;
    width: 660px;
    height: 3px;
    background: linear-gradient(90deg, rgba(255,255,255,0.2) 0%, rgba(255,255,255,0.6) 35%, var(--white) 100%);
  }
  .attorney-photos {
    position: absolute;
    left: 20px;
    top: 4px;
    width: 405px;
    height: 374px;
    background: linear-gradient(180deg, var(--brand-light) 0%, var(--brand-mid) 40%, #1c3f7a 100%);
    border-radius: 120px 120px 0 0;
  }
  .firm-name {
    position: absolute;
    left: 690px;
    top: 44px;
    width: 540px;
    text-align: center;
    font-weight: 700;
    font-size: 44px;
    letter-spacing: 8px;
    line-height: 1;
  }
  .firm-tagline {
    position: absolute;
    left: 690px;
    top: 108px;
    width: 540px;
    text-align: center;
    font-weight: 400;
    font-size: 15px;
    letter-spacing: 4px;
  }
  .headline {
    position: absolute;
    left: 430px;
    top: 163px;
    width: 810px;
    text-align: center;
    color: var(--brand-blue);
    font-weight: 700;
    line-height: 1;
  }
  .headline-main {
    display: block;
    font-size: 58px;
    letter-spacing: -0.5px;
  }
  .headline-sub {
    display: block;
    margin-top: 6px;
    font-size: 52px;
    letter-spacing: 28px;
    padding-left: 28px;
  }
  .phone {
    position: absolute;
    left: 430px;
    top: 300px;
    width: 810px;
    text-align: center;
    font-weight: 700;
    font-size: 52px;
    line-height: 1;
  }
</style>
</head>
<body>
  <main class="canvas">
    <section class="billboard">
      <div class="band-fade"></div>
      <div class="headline-band"></div>
      <div class="accent-rule"></div>
      <div class="attorney-photos" role="img" aria-label="Portrait of the firm's two attorneys in suits, arms crossed"></div>

      <div class="firm-name">QUARRY REED</div>
      <div class="firm-tagline">ATTORNEYS AT LAW</div>

      <h1 class="headline">
        <span class="headline-main">CRIMINAL AND PROBATION</span>
        <span class="headline-sub">DEFENSE</span>
      </h1>

      <div class="phone">(770) 555-0148</div>
    </section>
  </main>
</body>
</html>
```